Carpet Cleaning Door Hanger Design Project

please design a door hanger for us. we do carpet cleaning. our company name is Bright Loom Fibers. our telephone number is 866-430-2715.

please make a special offer coupon.

please add bullets containing the following info-
Professional carpet, hardwood, tile & grout deep steam cleaning.
kid & pet safe.
fast drying.
100% eco friendly / toxin free products.
pet stain/s & odor control.
same day appointments.
clean uniformed employees.
and please put few other catchy lines.

please make a $20.00 of carpet cleaning coupon (restrictions apply).
please make a rooms starting at $59.99 (restrictions apply).

please also put- when you want the best for less call bright loom fibers.

Target Market(s)

home owners, home renters. new home buyers. new home sellers.

Industry/Entity Type

Home Improvement

Requirements
Must have
• special offer.
• double sided.
• must be a design for a door hanger.
Nice to have
• 100% satisfaction guaranteed bubble.
Should not have
• no website please

```html
<!DOCTYPE html>
<html lang="en">
<head>
<meta charset="utf-8">
<title>Bright Loom Fibers – Door Hanger</title>
<link href="https://fonts.googleapis.com/css2?family=Archivo+Black&family=Open+Sans:wght@700;800&family=Oswald:wght@500;600&family=Roboto:ital,wght@1,900&display=swap" rel="stylesheet">
<style>
  :root{
    --purple:#3f1077;
    --red:#c8252c;
    --red-dark:#a51d2a;
    --white:#ffffff;
    --ink:#111111;
    --gold:#e5b21f;
    --page:#ffffff;
  }
  *{box-sizing:border-box;margin:0;padding:0}
  html,body{width:1200px;height:1200px;overflow:hidden;background:var(--page)}
  .canvas{position:relative;width:1200px;height:1200px}
  .hanger{position:absolute;background:var(--purple);overflow:hidden;box-shadow:6px 8px 10px rgba(0,0,0,.35)}
  .hanger--front{left:160px;top:68px;width:412px;height:1064px}
  .hanger--back{left:626px;top:62px;width:416px;height:1074px}
  .hanger__art{position:absolute;left:0;top:0}
  .brand{position:absolute;left:0;width:100%;text-align:center;font-family:"Archivo Black",sans-serif;color:var(--white);line-height:1;text-transform:uppercase;letter-spacing:-.5px}
  .brand__line{display:block;font-size:37px}
  .brand__line + .brand__line{margin-top:6px;font-size:44px}
  .front-brand{top:180px}
  .back-brand{top:910px}
  .tagline-reliable{position:absolute;left:100px;top:670px;width:260px;text-align:center;font-family:"Roboto",sans-serif;font-style:italic;font-weight:900;color:var(--red);line-height:1;text-transform:uppercase}
  .tagline-reliable span{display:block;font-size:22px}
  .tagline-reliable span + span{font-size:32px;margin-top:-2px}
  .features{position:absolute;left:40px;top:778px;list-style:none}
  .features li{display:flex;align-items:center;height:26.3px;font-family:"Roboto",sans-serif;font-style:italic;font-weight:900;font-size:14.5px;color:var(--white)}
  .features svg{width:14px;height:14px;margin-right:8px;flex:none}
  .rule{position:absolute;left:27px;width:358px;height:1px;background:rgba(255,255,255,.8)}
  .front-rule{top:990px}
  .back-rule{top:1015px;left:27px;width:360px}
  .call-today{position:absolute;top:1000px;width:100%;text-align:center;font-family:"Roboto",sans-serif;font-style:italic;font-weight:900;font-size:14px;color:var(--white);letter-spacing:.5px}
  .phone{position:absolute;width:100%;text-align:center;font-family:"Roboto",sans-serif;font-style:italic;font-weight:900;font-size:33px;color:var(--red);letter-spacing:-.5px}
  .front-phone{top:1018px}
  .back-phone{top:1028px}
  .ribbon-text{position:absolute;left:30px;width:354px;text-align:center;font-family:"Open Sans",sans-serif;font-weight:800;font-size:48px;color:var(--white);line-height:1}
  .ribbon-special{top:333px}
  .ribbon-offer{top:432px}
  .coupon{position:absolute;top:555px;height:141px;background:var(--white);border-left:2px dashed #555;border-right:2px dashed #555;border-bottom:3px solid var(--ink)}
  .coupon--carpet{left:16px;width:187px}
  .coupon--rooms{left:210px;width:188px}
  .coupon__title{height:38px;background:var(--purple);color:var(--white);font-family:"Oswald",sans-serif;font-weight:500;font-size:22px;text-align:center;line-height:38px;letter-spacing:-.3px}
  .coupon__from{position:absolute;left:10px;top:42px;font-family:"Oswald",sans-serif;font-weight:500;font-size:18px;color:var(--red)}
  .coupon__price{position:absolute;left:6px;right:4px;bottom:4px;display:flex;align-items:baseline;font-family:"Oswald",sans-serif;font-weight:600;color:var(--ink);line-height:1}
  .coupon__currency{font-size:34px;color:var(--purple);margin-right:8px}
  .coupon__amount{font-size:64px;letter-spacing:-2px}
  .best-for-less{position:absolute;top:758px;width:100%;text-align:center;font-family:"Archivo Black",sans-serif;line-height:1;text-transform:uppercase}
  .best-for-less .lead{display:block;color:var(--red);font-size:24px}
  .best-for-less .main{display:block;color:var(--purple);font-size:38px;margin-top:1px}
  .best-for-less .call{display:block;color:var(--red);font-size:23px;margin-top:1px}
</style>
</head>
<body>
<div class="canvas">

  <!-- Front side -->
  <section class="hanger hanger--front">
    <svg class="hanger__art" width="412" height="1064" viewBox="0 0 412 1064">
      <line x1="124" y1="0" x2="172" y2="46" stroke="#fff" stroke-width="2" stroke-dasharray="6 5"/>
      <circle cx="210" cy="96" r="61" fill="none" stroke="#fff" stroke-width="2" stroke-dasharray="6 5"/>
      <g role="img" aria-label="Photo of a smiling girl lying on a fluffy carpet with a golden retriever, with a vacuum cleaner head on the carpet">
        <defs>
          <linearGradient id="photoFront" x1="0" y1="0" x2="0" y2="1">
            <stop offset="0" stop-color="#e9e3e6"/>
            <stop offset=".45" stop-color="#e6d9b8"/>
            <stop offset="1" stop-color="#efe8df"/>
          </linearGradient>
        </defs>
        <path d="M0 296 Q206 336 412 284 L412 752 Q220 830 0 730 Z" fill="url(#photoFront)"/>
      </g>
      <path d="M0 282 Q206 330 412 270 L412 284 Q206 340 0 308 Z" fill="var(--red)"/>
      <path d="M0 730 Q220 830 412 752 L412 790 Q330 808 270 800 Q340 800 412 780 L412 1064 L0 1064 Z" fill="var(--purple)"/>
      <path d="M170 770 Q300 790 412 722 L412 750 Q300 808 170 770 Z" fill="var(--red)"/>
      <path d="M0 690 A120 140 0 0 1 190 650" fill="none" stroke="var(--red)" stroke-width="6"/>
      <g aria-hidden="true">
        <circle cx="88" cy="404" r="78" fill="var(--gold)"/>
        <circle cx="88" cy="404" r="52" fill="#2a2a2a"/>
        <circle cx="88" cy="404" r="30" fill="#e8e2d0"/>
      </g>
    </svg>

    <h1 class="brand front-brand"><span class="brand__line">Bright Loom</span><span class="brand__line">Fibers</span></h1>

    <p class="tagline-reliable"><span>Reliable Carpet</span><span>Cleaning</span></p>

    <ul class="features">
      <li><svg viewBox="0 0 14 14"><circle cx="7" cy="7" r="6" fill="none" stroke="#fff" stroke-width="1.4"/><path d="M4 7.2l2.2 2.2L10.5 4" fill="none" stroke="#e33" stroke-width="1.8"/></svg>Professional Carpet, Hardwood</li>
      <li><svg viewBox="0 0 14 14"><circle cx="7" cy="7" r="6" fill="none" stroke="#fff" stroke-width="1.4"/><path d="M4 7.2l2.2 2.2L10.5 4" fill="none" stroke="#e33" stroke-width="1.8"/></svg>Tile &amp; Grout Deep Steam Cleaning.</li>
      <li><svg viewBox="0 0 14 14"><circle cx="7" cy="7" r="6" fill="none" stroke="#fff" stroke-width="1.4"/><path d="M4 7.2l2.2 2.2L10.5 4" fill="none" stroke="#e33" stroke-width="1.8"/></svg>Kid &amp; Pet Safe.</li>
      <li><svg viewBox="0 0 14 14"><circle cx="7" cy="7" r="6" fill="none" stroke="#fff" stroke-width="1.4"/><path d="M4 7.2l2.2 2.2L10.5 4" fill="none" stroke="#e33" stroke-width="1.8"/></svg>Fast Drying.</li>
      <li><svg viewBox="0 0 14 14"><circle cx="7" cy="7" r="6" fill="none" stroke="#fff" stroke-width="1.4"/><path d="M4 7.2l2.2 2.2L10.5 4" fill="none" stroke="#e33" stroke-width="1.8"/></svg>100% Eco Friendly / Toxin Free Products.</li>
      <li><svg viewBox="0 0 14 14"><circle cx="7" cy="7" r="6" fill="none" stroke="#fff" stroke-width="1.4"/><path d="M4 7.2l2.2 2.2L10.5 4" fill="none" stroke="#e33" stroke-width="1.8"/></svg>Pet Stand &amp; Odor Control.</li>
      <li><svg viewBox="0 0 14 14"><circle cx="7" cy="7" r="6" fill="none" stroke="#fff" stroke-width="1.4"/><path d="M4 7.2l2.2 2.2L10.5 4" fill="none" stroke="#e33" stroke-width="1.8"/></svg>Same Day Appointments.</li>
      <li><svg viewBox="0 0 14 14"><circle cx="7" cy="7" r="6" fill="none" stroke="#fff" stroke-width="1.4"/><path d="M4 7.2l2.2 2.2L10.5 4" fill="none" stroke="#e33" stroke-width="1.8"/></svg>Clean Uniformed Employees.</li>
    </ul>

    <div class="rule front-rule"></div>
    <p class="call-today">CALL US TODAY</p>
    <p class="phone front-phone">866-430-2715</p>
  </section>

  <!-- Back side -->
  <section class="hanger hanger--back">
    <svg class="hanger__art" width="416" height="1074" viewBox="0 0 416 1074">
      <g role="img" aria-label="Photo of a bright living room with a white sofa and a thick grey shag carpet">
        <defs>
          <linearGradient id="photoBack" x1="0" y1="0" x2="0" y2="1">
            <stop offset="0" stop-color="#e6e4e0"/>
            <stop offset=".3" stop-color="#c9c5bf"/>
            <stop offset=".5" stop-color="#a79d93"/>
            <stop offset="1" stop-color="#968a7f"/>
          </linearGradient>
        </defs>
        <rect x="0" y="170" width="416" height="780" fill="url(#photoBack)"/>
      </g>
      <path d="M0 0 H416 V180 Q220 250 0 190 Z" fill="var(--purple)"/>
      <path d="M0 190 Q150 232 330 222 Q190 250 0 232 Z" fill="var(--red)"/>
      <line x1="302" y1="0" x2="254" y2="50" stroke="#fff" stroke-width="2" stroke-dasharray="6 5"/>
      <circle cx="212" cy="99" r="61" fill="none" stroke="#fff" stroke-width="2" stroke-dasharray="6 5"/>
      <polygon points="30,323 384,323 384,394 30,394 54,358" fill="var(--red)"/>
      <polygon points="60,394 384,394 384,410 30,422" fill="var(--red-dark)"/>
      <polygon points="30,422 384,422 360,456 384,491 30,491" fill="var(--red)"/>
      <path d="M0 915 Q200 840 416 885 L416 1074 L0 1074 Z" fill="var(--red)"/>
      <path d="M0 935 Q200 870 416 912 L416 1074 L0 1074 Z" fill="var(--purple)"/>
    </svg>

    <p class="ribbon-text ribbon-special">SPECIAL</p>
    <p class="ribbon-text ribbon-offer">OFFER</p>

    <div class="coupon coupon--carpet">
      <div class="coupon__title">CARPET CLEANING</div>
      <div class="coupon__price"><span class="coupon__currency">$</span><span class="coupon__amount">20.00</span></div>
    </div>
    <div class="coupon coupon--rooms">
      <div class="coupon__title">ROOMS CLEANING</div>
      <span class="coupon__from">FROM:</span>
      <div class="coupon__price"><span class="coupon__currency">$</span><span class="coupon__amount">59.99</span></div>
    </div>

    <p class="best-for-less"><span class="lead">When you want the</span><span class="main">Best for less</span><span class="call">Call</span></p>

    <h2 class="brand back-brand"><span class="brand__line">Bright Loom</span><span class="brand__line">Fibers</span></h2>
    <div class="rule back-rule"></div>
    <p class="phone back-phone">866-430-2715</p>
  </section>

</div>
</body>
</html>
```